Website Redesign For Marketing Agency

www.brightlanepromoworks.biz

Please start with home page only. Use EXACT SAME CONTENT

If you want me to consider design please provide me full homepage with exact content provided in original url

Target Market(s)

business owners b2b

Industry/Entity Type

Digital Marketing

Number of Pages Required

5+ page

Requirements
Must have
• exact same content
Nice to have
• exact same elements throughout
Should not have
• make redesign website using all exact same copy

```html
<!DOCTYPE html>
<html lang="en">
<head>
<meta charset="utf-8">
<title>Brightlane Promoworks – Marketing Incentives</title>
<link rel="stylesheet" href="https://fonts.googleapis.com/css2?family=Rubik:wght@500;700;900&family=Roboto:wght@400;500;700&family=Open+Sans:wght@500&display=swap">
<style>
:root{
  --topbar:#4d4d4f;
  --red:#d00d0d;
  --blue:#1270bf;
  --blue-dark:#0f5fa6;
  --heading-blue:#1d7fd4;
  --green:#4aa84a;
  --green-text:#4fae48;
  --ink:#2b2b2b;
  --body:#444;
  --panel:#f2f2f3;
  --line:#2f2f2f;
}
*{box-sizing:border-box;margin:0;padding:0}
html,body{width:1200px;height:3745px;overflow:hidden;background:#fff}
body{font-family:"Roboto",sans-serif;color:var(--body);position:relative}
.abs{position:absolute}

.topbar{left:0;top:0;width:1200px;height:44px;background:var(--topbar);color:#fff;font-size:13px}
.topbar .item{position:absolute;top:14px;display:flex;align-items:center;gap:7px}
.topbar svg{width:13px;height:13px;fill:#fff}

.nav{left:0;top:44px;width:1200px;height:78px;background:#fff}
.brand{position:absolute;left:116px;top:24px;display:flex;align-items:center;gap:9px;font-family:"Rubik",sans-serif;font-weight:700;font-size:20px;color:var(--blue)}
.brand .dot{width:18px;height:18px;background:var(--blue);border-radius:50%}
.menu{position:absolute;right:122px;top:30px;display:flex;gap:22px;font-size:15px;color:#222}

.headline{left:23px;top:122px;width:1152px;height:94px;background:var(--red);border-radius:6px 6px 0 0;color:#fff;font-family:"Rubik",sans-serif;font-weight:900;font-size:52px;text-align:center;line-height:94px;letter-spacing:-.3px}
.banner{left:0;top:215px;width:1200px;height:165px}
.banner-sub{left:0;top:232px;width:1200px;text-align:center;color:#fff;font-family:"Rubik",sans-serif;font-weight:500;font-size:25px}
.perks{left:230px;top:287px;display:flex;gap:48px;color:#fff;font-family:"Rubik",sans-serif;font-weight:500;font-size:18px;line-height:20px}
.perk{display:flex;align-items:center;gap:12px}
.perk svg{width:50px;height:42px;fill:#fff}

.hero{left:0;top:355px;width:1200px;height:300px;background:linear-gradient(#fff,#e4e4e6 70%,#d2d2d4)}
.flyers{left:44px;top:364px;width:1112px;height:272px;background:linear-gradient(90deg,#e9e9ea,#c63a33 18%,#ededee 35%,#b7472f 55%,#f1f1f1 72%,#c74b4b 88%,#e4e4e4);opacity:.55;border-radius:2px}
.btn{display:block;background:var(--blue);color:#fff;font-family:"Roboto",sans-serif;font-weight:500;font-size:17px;text-align:center;letter-spacing:.2px;border-radius:3px}
.hero-btn{left:432px;top:558px;width:335px;height:64px;line-height:64px}

.incentives{left:0;top:655px;width:1200px;height:1425px;background:var(--panel)}
.h2{position:absolute;left:0;width:1200px;text-align:center;font-family:"Rubik",sans-serif;font-weight:700;color:var(--ink)}
.h2 .b{color:var(--heading-blue)}
.inc-title{top:780px;font-size:46px;line-height:53px;letter-spacing:-.2px}
.inc-sub{left:200px;top:970px;width:800px;text-align:center;color:var(--green-text);font-family:"Open Sans",sans-serif;font-weight:500;font-size:18px;line-height:23px}

.card{position:absolute;width:243px;height:440px;background:#fff;box-shadow:0 1px 3px rgba(0,0,0,.08)}
.card .photo{height:246px;position:relative;display:flex;align-items:flex-end;justify-content:center;padding-bottom:27px}
.card .photo span{color:#fff;font-family:"Roboto",sans-serif;font-weight:700;font-size:17px;line-height:21px;text-align:center;text-transform:uppercase;text-shadow:0 1px 3px rgba(0,0,0,.5)}
.card p{padding:22px 12px 0;font-size:14px;line-height:29px;text-align:center;color:#444}
.card p b{color:var(--blue);font-weight:700}

.adv-title{top:2212px;font-size:46px;line-height:53px}

.node{position:absolute;width:72px;height:72px;border-radius:50%;border:3px solid #fff;box-shadow:0 0 0 2px currentColor;display:flex;align-items:center;justify-content:center}
.node svg{width:38px;height:38px;stroke:#fff;fill:none;stroke-width:2}
.node.blue{background:var(--blue);color:var(--blue)}
.node.green{background:var(--green);color:var(--green)}

.box{position:absolute;color:#fff;padding:20px 17px;border-radius:3px}
.box.blue{background:var(--blue)}
.box.green{background:var(--green)}
.box h3{font-family:"Roboto",sans-serif;font-weight:700;font-size:17px;line-height:26px;margin-bottom:14px}
.box h3 u{text-underline-offset:2px}
.box p{font-size:13.3px;line-height:27px;letter-spacing:.6px}

.closing{left:0;top:3540px;width:1200px;text-align:center;font-size:24px;line-height:31px;color:#222}
.end-btn{left:432px;top:3654px;width:335px;height:63px;line-height:63px}
.footer-strip{left:0;top:3740px;width:1200px;height:5px;background:#eee}
</style>
</head>
<body>

<header class="abs topbar">
  <div class="item" style="left:113px"><svg viewBox="0 0 24 24"><path d="M6.6 10.8a15 15 0 006.6 6.6l2.2-2.2a1 1 0 011-.25 11.4 11.4 0 003.6.57 1 1 0 011 1V20a1 1 0 01-1 1A17 17 0 013 4a1 1 0 011-1h3.5a1 1 0 011 1c0 1.25.2 2.45.57 3.6a1 1 0 01-.25 1z"/></svg>1-555-014-2277</div>
  <div class="item" style="left:257px"><svg viewBox="0 0 24 24"><path d="M4 8h16v12H4zM7 4h10v3H7z"/></svg>1-555-019-4410</div>
  <div class="item" style="left:936px"><svg viewBox="0 0 24 24"><circle cx="12" cy="7" r="5"/><path d="M2 23c0-6 4-9 10-9s10 3 10 9z"/></svg>Login</div>
  <div class="item" style="left:1008px"><svg viewBox="0 0 24 24"><circle cx="10" cy="7" r="5"/><path d="M0 23c0-6 4-9 10-9s10 3 10 9zM19 4h2v3h3v2h-3v3h-2V9h-3V7h3z"/></svg>Sign Up</div>
</header>

<nav class="abs nav">
  <div class="brand"><span class="dot"></span>Brightlane Promoworks</div>
  <div class="menu"><span>Home</span><span>The Incentives</span><span>Demo Videos</span><span>Autoflow</span><span>Industries</span><span>Faq</span><span>Pricing</span><span>Testimonials</span></div>
</nav>

<svg class="abs banner" viewBox="0 215 1200 165" aria-hidden="true"><path d="M23 215H1177V300Q1177 332 1146 335L600 378L54 335Q23 332 23 300Z" fill="#0c5fb0"/></svg>
<h1 class="abs headline">INCREASE LEADS &amp; SALES OVERNIGHT</h1>
<div class="abs banner-sub">Attract New Customers With High Perceived Value Marketing Incentives</div>
<div class="abs perks">
  <div class="perk"><svg viewBox="0 0 50 42"><rect x="14" y="4" width="30" height="24" rx="2"/><rect x="4" y="16" width="12" height="22" rx="2"/><rect x="18" y="30" width="22" height="6"/></svg>Smart<br>Devices</div>
  <div class="perk"><svg viewBox="0 0 50 42"><rect x="2" y="6" width="46" height="30" rx="4"/><text x="25" y="30" font-size="24" font-weight="700" text-anchor="middle" fill="#0c5fb0" font-family="Arial">%</text></svg>Dining<br>Vouchers</div>
  <div class="perk"><svg viewBox="0 0 50 42"><rect x="4" y="4" width="42" height="34" rx="2"/><rect x="9" y="10" width="32" height="3" fill="#0c5fb0"/><rect x="9" y="17" width="24" height="3" fill="#0c5fb0"/><rect x="9" y="24" width="28" height="3" fill="#0c5fb0"/></svg>Vacation<br>Certificates</div>
  <div class="perk"><svg viewBox="0 0 50 42"><rect x="18" y="4" width="12" height="10"/><rect x="10" y="14" width="30" height="10"/><path d="M2 24H48L42 36H8Z"/></svg>Cruise<br>Incentives</div>
</div>

<div class="abs hero"></div>
<div class="abs flyers" role="img" aria-label="Row of printed promotional incentive flyers for vacations, dining, smart devices and cruises"></div>
<a class="abs btn hero-btn">GET A FREE SAMPLE PACKAGE</a>

<section class="abs incentives"></section>
<h2 class="h2 inc-title">UNLIMITED MARKETING INCENTIVES<br>GUARANTEED TO <span class="b">ATTRACT MORE<br>CUSTOMERS FOR YOUR BUSINESS</span></h2>
<p class="abs inc-sub">By Creating Exciting Promotional Giveaways Using An Unlimited Amount Of Gift Certificates Redeemable For:</p>

<div class="card" style="left:103px;top:1087px"><div class="photo" role="img" aria-label="Luggage on a beach terrace" style="background:linear-gradient(#bcdbe8,#5aa3b8 55%,#2d5563)"><span>Unlimited Vacation<br>Certificates</span></div><p>Resort Stays, Cruises &amp; Airfares Up To <b>$3,000.00 Retail Value.</b> Your Customers Just Pay Fees &amp; Taxes!</p></div>
<div class="card" style="left:353px;top:1087px"><div class="photo" role="img" aria-label="Table of shared restaurant dishes" style="background:linear-gradient(#8a7262,#5b4638 60%,#2e231c)"><span>Unlimited Dining<br>Takeout Vouchers</span></div><p><b>$25-$500 True Cash Value</b> at Thousands Of Restaurants Nationwide. Accepted For Takeout Too!</p></div>
<div class="card" style="left:604px;top:1087px"><div class="photo" role="img" aria-label="Smartphone and smart watch with charts" style="background:linear-gradient(#8b8f94,#4c5055 60%,#1e2023)"><span>Unlimited Smart Device<br>Giveways</span></div><p>Tablets, Earbuds, Smart Watches, UV Smartphone Sterilizers, Mp4 Players and More <b>$129-$199 Retail Value</b></p></div>
<div class="card" style="left:854px;top:1087px"><div class="photo" role="img" aria-label="Cruise ship at sea" style="background:linear-gradient(#a9c3dc,#6b8eaf 55%,#1d3245)"><span>Unlimited Cruise<br>Incentives</span></div><p>2 Night &amp; 4 Night Luxury All Inclusive Cruises To The Mexican Riviera, Carribean and The Bahamas. <b>Up to $1,233 Retail Value</b></p></div>

<div class="card" style="left:103px;top:1549px"><div class="photo" role="img" aria-label="Keyboard with a book now key" style="background:linear-gradient(135deg,#e3e5e7,#9aa2a8 55%,#3a6fa8)"><span>Unlimited Airfare<br>Incentives</span></div><p>All Inclusive Resorts, Over 3500 Properties Around The World. For Domestic &amp; International Travel. <b>Up to $2,188 Retail Value</b></p></div>
<div class="card" style="left:353px;top:1549px"><div class="photo" role="img" aria-label="Palm trees over a resort beach" style="background:linear-gradient(#4f8fb5,#3b7a5c 55%,#25402f)"><span>Unlimited Resort<br>Certificates</span></div><p>All Inclusive Resorts, Over 3500 Properties Around The World. For Domestic &amp; International Travel. <b>Up to $2,188 Retail Value</b></p></div>
<div class="card" style="left:604px;top:1549px"><div class="photo" role="img" aria-label="Resort buildings and pool at dusk" style="background:linear-gradient(#9fb4c9,#5d6f7d 55%,#1f2a33)"><span>Unlimited All Inclusive<br>Certificates</span></div><p>5 Star Luxury Resorts With All Inclusive Packages. Vacations With Airfare Included. All Inclusive Vacations. <b>Up to $3,122 Retail Value</b></p></div>
<div class="card" style="left:854px;top:1549px"><div class="photo" role="img" aria-label="Glass jar filled with cash" style="background:linear-gradient(#dcdcd6,#9fa08a 55%,#3c3d33)"><span>Unlimited Discount<br>Savings Incentives</span></div><p>BOGO's, Discounts and Savings On Golf, Dining, Fast Food, Groceries, Personal Care Items, Wine, Pro Teeth Whitening Kits, Fitness &amp; More! <b>Unlimited Savings Potential</b></p></div>

<h2 class="h2 adv-title">The 4 Major Advertising Areas That Matter<br>Most <span class="b">to Your Business and How Brightlane<br>Seamlessly Integrates with Them…</span></h2>

<svg class="abs" style="left:0;top:2450px" width="1200" height="1080" viewBox="0 2450 1200 1080" aria-hidden="true" fill="none" stroke-width="5">
  <path d="M180 2467H584Q599 2467 599 2482V3517" stroke="var(--line)"/>
  <path d="M215 2467V2532M496 2467V2532" stroke="var(--blue)"/>
  <path d="M1015 2583H614Q599 2583 599 2598" stroke="var(--line)"/>
  <path d="M704 2583V2647M988 2583V2647" stroke="var(--green)"/>
  <path d="M180 2916H584Q599 2916 599 2931" stroke="var(--line)"/>
  <path d="M215 2916V2982M496 2916V2982" stroke="var(--green)"/>
  <path d="M1015 3033H614Q599 3033 599 3048" stroke="var(--line)"/>
  <path d="M704 3033V3095M988 3033V3095" stroke="var(--blue)"/>
</svg>

<div class="node blue" style="left:114px;top:2427px"><svg viewBox="0 0 38 38"><path d="M4 20Q19 6 34 20Q19 30 4 20Z"/><circle cx="19" cy="19" r="4"/><path d="M8 34V28M14 34V25M20 34V27M26 34V22"/></svg></div>
<div class="node green" style="left:1014px;top:2539px"><svg viewBox="0 0 38 38"><circle cx="22" cy="13" r="9"/><path d="M22 8V18M3 28L12 24H22L30 20M3 33H20L34 25"/></svg></div>
<div class="node green" style="left:114px;top:2876px"><svg viewBox="0 0 38 38"><circle cx="19" cy="12" r="9"/><path d="M19 7V17M7 35V27M14 35V23M24 35V23M31 35V27"/></svg></div>
<div class="node blue" style="left:1014px;top:2989px"><svg viewBox="0 0 38 38"><rect x="4" y="6" width="20" height="16"/><path d="M8 18L12 13L16 16L20 10M6 34L14 26M14 34L6 26M28 6H34V12M26 24H34V32H26Z"/></svg></div>

<div class="box blue" style="left:125px;top:2532px;width:463px;height:214px">
  <h3>Want to see an <u>explosion in response rates</u> of your existing ads?</h3>
  <p>Use one (or more) of the incentives that come with your Brightlane package as a simple tagline. For example: “When you contact us today you will receive a FREE Smartwatch, without spending a dime…”</p>
</div>
<div class="box green" style="left:612px;top:2647px;width:464px;height:294px">
  <h3>Did you know that “new customer acquisition” is THE <u>most expensive</u> advertising cost for a business? Well, at least it was…</h3>
  <p>When you have a product and/or a service that the marketplace wants and needs, but is on the fence about making a purchase, you can now offer them a high valued incentive like our “Airfare Plus Hotel Giveaway” or the “HD Tablet powered by NovaOS” to give them that extra nudge to buy today instead of in the future…</p>
</div>
<div class="box green" style="left:125px;top:2982px;width:463px;height:241px">
  <h3>13% or 300% : To your <u>bottom line</u>, which do you prefer?</h3>
  <p>According to Ledgerline Metrics, repeat customers spend 300% more money than new customers over time. And with your Brightlane package you have the customer appreciation incentivizes – Brand New UV Smartphone Sanitizer or $300 In Restaurant Takeout Cash – to come back for even more…</p>
</div>
<div class="box blue" style="left:612px;top:3095px;width:464px;height:405px">
  <h3>Are You Ready to <u>Supercharge The Most Powerful Marketing</u> of All? We hope so…</h3>
  <p>Because what do you think is going to happen when your product and/or service delivers on its promise AND you add High Valued Incentives to the deal? Yup, you guessed it… The Most Powerful Marketing of All; Word-of-Mouth : “Mr or Mrs Customer. We want to thank you for being part of our family and show our gratitude and appreciation. And for the next 24hrs, we are offering the first 25 people who go here, tag a friend and share this on their wall a $100 Wine Voucher. One lucky person will get a 7 Night Resort stay. Don't forget to hashtag #iLove YOURBUSINESS …” and watch your business explode!</p>
</div>

<p class="abs closing">But don’t believe our word for it. See for yourself…<br>Simply click the button below now and test drive a sample package 100% FREE!</p>
<a class="abs btn end-btn">GET A FREE SAMPLE PACKAGE</a>
<div class="abs footer-strip"></div>

</body>
</html>
```